"Beyond Marrow Cay" Fictional Book Cover

BEYOND MARROW CAY
By: Dale Pruitt

Here's the intro .

"It had been nearly forty years since Ted Larraby last went to the island from where he was raised. Three months earlier he never would have thought about ever coming back. But life is weird. Things happen quickly and plans change, especially when your very life is at stake. The reason he was going back wasn’t to see old friends...no, no, no. They’re all dead. Of all the kids he grew up with on the island who moved off, he’s the only one still alive. Why?"

Pretty much all just a Lumeno book, by the way.

Target Market(s)

fiction readers

Requirements
Must have
• Somewhat of a dark, mysterious cover is what I'd like to see. Use your imagination. I've never written a fiction book before so I'm very open to ideas

Needs to have my name, DALE PRUITT at the bottom. like my other books, all of which are non-fiction
Nice to have
• Mysterious is what I'm looking for. NOT A HORROR story though. More a guy who left the island years ago, but is being called back to escape the rat race of modern, consumerist culture.

Please remember this NEEDS to jump out as a thumbnail on Bookvale as people are browsing. Mainly the WORDS need to stick out. Lighter words on a say a blue background.

If you want to try to use the attached pic, or something like this, to reflect an island in the cover, that'd be good.

I've also uploaded a couple images I purchased from Pixelcrate, hopefully you can make something work with these.

```html
<!DOCTYPE html>
<html lang="en">
<head>
<meta charset="utf-8">
<title>Beyond Marrow Cay – Cover Wrap</title>
<link rel="stylesheet" href="https://fonts.googleapis.com/css2?family=Oranienbaum&family=Oswald:wght@300;500&display=swap">
<style>
  :root {
    --sky-top: #686868;
    --sky-low: #c9c9c9;
    --treeline: #3b3733;
    --autumn: #6e3a24;
    --shore: #8a8884;
    --water-top: #5e5f60;
    --water-low: #3d3e40;
    --title-white: #ffffff;
    --title-red: #c7332a;
    --ink-light: #f4f4f4;
    --shadow: rgba(0,0,0,0.45);
  }
  html, body {
    margin: 0;
    padding: 0;
    width: 1200px;
    height: 900px;
    overflow: hidden;
    background: #222;
  }
  .cover-wrap {
    position: relative;
    width: 1200px;
    height: 900px;
    overflow: hidden;
  }
  .scene-photo {
    position: absolute;
    inset: 0;
    background:
      radial-gradient(ellipse 520px 90px at 900px 480px, var(--autumn) 0%, transparent 70%),
      linear-gradient(to bottom,
        var(--sky-top) 0%,
        #9a9a9a 18%,
        var(--sky-low) 38%,
        #b8b8b8 46%,
        var(--treeline) 52%,
        #4a4440 60%,
        var(--shore) 63%,
        var(--water-top) 66%,
        #525354 80%,
        var(--water-low) 100%);
  }
  .title-art {
    position: absolute;
    inset: 0;
  }
  .title-art text {
    font-family: "Oranienbaum", "Times New Roman", serif;
  }
  .title-white { fill: var(--title-white); }
  .title-red { fill: var(--title-red); }
  .back-blurb {
    position: absolute;
    left: 88px;
    top: 228px;
    width: 396px;
    margin: 0;
    font-family: "Oswald", "Arial Narrow", sans-serif;
    font-weight: 300;
    font-size: 20.5px;
    line-height: 26.8px;
    color: var(--ink-light);
    text-align: center;
    text-shadow: 0 1px 2px var(--shadow);
  }
  .back-blurb strong {
    font-weight: 500;
    font-style: italic;
  }
  .author-bio {
    position: absolute;
    left: 84px;
    top: 505px;
    width: 406px;
    margin: 0;
    font-family: "Oswald", "Arial Narrow", sans-serif;
    font-weight: 300;
    font-size: 17px;
    line-height: 23.4px;
    color: var(--ink-light);
    text-align: center;
    text-shadow: 0 1px 2px var(--shadow);
  }
  .author-bio strong {
    font-weight: 500;
    font-style: italic;
  }
  .isbn-box {
    position: absolute;
    left: 332px;
    top: 746px;
    width: 200px;
    height: 120px;
    background: #ffffff;
  }
</style>
</head>
<body>
<main class="cover-wrap">
  <div class="scene-photo" role="img" aria-label="Muted grey photograph of a wooded island shoreline with autumn-red trees, white cottages and a red-roofed pavilion above dark grey sea water, with a small buoy"></div>

  <svg class="title-art" width="1200" height="900" viewBox="0 0 1200 900" aria-label="Beyond Marrow Cay by Dale Pruitt">
    <defs>
      <filter id="title-shadow" x="-5%" y="-10%" width="110%" height="130%">
        <feDropShadow dx="2" dy="3" stdDeviation="2" flood-color="#000" flood-opacity="0.45"/>
      </filter>
    </defs>

    <!-- back cover title -->
    <g class="back-title" filter="url(#title-shadow)">
      <text class="title-white" x="156" y="136" font-size="78" textLength="260" lengthAdjust="spacingAndGlyphs">BEYOND</text>
      <text class="title-red" x="150" y="192" font-size="68" textLength="274" lengthAdjust="spacingAndGlyphs">MARROW CAY</text>
    </g>

    <!-- spine -->
    <g class="spine" filter="url(#title-shadow)">
      <text transform="translate(580 56) rotate(90)" font-size="46">
        <tspan class="title-white">BEYOND </tspan><tspan class="title-red">MARROW CAY</tspan>
      </text>
      <text class="title-white" transform="translate(581 680) rotate(90)" font-size="46" textLength="184" lengthAdjust="spacingAndGlyphs">Dale Pruitt</text>
    </g>

    <!-- front cover -->
    <g class="front-title" filter="url(#title-shadow)">
      <text class="title-white" x="688" y="196" font-size="146" textLength="448" lengthAdjust="spacingAndGlyphs">BEYOND</text>
      <text class="title-red" x="692" y="292" font-size="112" textLength="440" lengthAdjust="spacingAndGlyphs">MARROW CAY</text>
      <text class="title-white" x="756" y="864" font-size="86" textLength="312" lengthAdjust="spacingAndGlyphs">Dale Pruitt</text>
    </g>
  </svg>

  <p class="back-blurb">"It had been nearly forty years since Ted Larraby last went to the island from where he was raised. Three months earlier he never would have thought about ever coming back. But life is weird. Things happen quickly and plans change, especially when your very life is at stake. The reason he was going back wasn’t to see old friends...no, no, no. They’re all dead. Of all the kids he grew up with on the island who moved off, he’s the only one still alive. <strong>Why?</strong>"</p>

  <p class="author-bio"><strong>Dale</strong> greatly values spending time with his wife and four children. He has served for many years as a volunteer coach in his children’s sports activities. His family is also very active in their church and neighborhood community. Being raised on a small island in Casco Bay, Maine, Dale is a passionate fan of college and professional hockey and tries to catch a Harbor City Gulls game at least once a year with his family.</p>

  <div class="isbn-box"></div>
</main>
</body>
</html>
```